English and Spanish Language School Needs a Business Card

Need a business card design a startup company called Meridel Language School. The company will offer English and Spanish conversational level courses designed to make the learner feel comfortable with grammar and vocabulary. We would like to see a logo with some colour that should communicate learning, growth.

Target Market(s)

Consumers and businesses

Industry/Entity Type

Education

Contact Information for Business Card

TBD

Font styles to use
Serif

Requirements
Must have
• Include the following
• Logo
• Name
• Title
• Cellphone Number
• Office Phone number
• Email address
• Office Address

```html
<!DOCTYPE html>
<html lang="en">
<head>
<meta charset="utf-8">
<title>Meridel Language School – Business Card</title>
<link rel="stylesheet" href="https://fonts.googleapis.com/css2?family=Montserrat:wght@400;600;700;800&display=swap">
<style>
  :root {
    --teal: #0aa1ab;
    --red: #d0202f;
    --white: #ffffff;
    --stage: #e9ecee;
    --shadow: rgba(0, 0, 0, 0.18);
  }
  * { margin: 0; padding: 0; box-sizing: border-box; }
  html, body {
    width: 1200px; height: 900px; overflow: hidden;
    background: var(--stage);
    font-family: "Montserrat", sans-serif;
  }
  .canvas { position: relative; width: 1200px; height: 900px; }
  .card {
    position: absolute;
    width: 680px; height: 390px;
    border-radius: 26px;
    box-shadow: 0 10px 28px var(--shadow);
    overflow: hidden;
  }
  .card--front { left: 80px; top: 40px; background: var(--teal); color: var(--white); }
  .card--back { left: 440px; top: 470px; background: var(--white); }

  .brand-name {
    font-weight: 800;
    line-height: 0.95;
    letter-spacing: -1px;
  }
  .card--front .brand-name {
    position: absolute; left: 0; right: 0; top: 110px;
    text-align: center; font-size: 82px; color: var(--white);
  }
  .card--front .brand-name span { display: block; font-size: 34px; letter-spacing: 0; margin-top: 6px; }
  .website-front {
    position: absolute; left: 0; right: 0; bottom: 40px;
    text-align: center; font-size: 17px; font-weight: 600; letter-spacing: 0.5px;
  }

  .card--back .brand-name {
    position: absolute; left: 50px; top: 120px;
    font-size: 62px; color: var(--red);
  }
  .card--back .brand-name span { display: block; font-size: 25px; letter-spacing: 0; margin-top: 6px; }

  .contact {
    position: absolute; left: 400px; top: 100px;
    color: var(--teal); font-size: 16px; line-height: 1.45;
  }
  .contact__name { color: var(--red); font-weight: 700; font-size: 24px; line-height: 1.2; }
  .contact__title { font-size: 15px; margin-bottom: 8px; }
  .contact__address { margin-bottom: 8px; }
  .contact__row { display: flex; align-items: center; gap: 10px; }
  .contact__row svg { width: 14px; height: 14px; flex: none; }
  .contact__web { color: var(--red); font-weight: 700; }
</style>
</head>
<body>
<main class="canvas">
  <section class="card card--front" aria-label="Card front">
    <div class="brand-name">Meridel<span>Language School</span></div>
    <div class="website-front">www.meridelschool.com</div>
  </section>

  <section class="card card--back" aria-label="Card back">
    <div class="brand-name">Meridel<span>Language School</span></div>
    <div class="contact">
      <div class="contact__name">Tomas Halvorsen</div>
      <div class="contact__title">Director</div>
      <div class="contact__address">Po Box 218<br>Ashcombe VIC 3902</div>
      <div class="contact__row">
        <svg viewBox="0 0 14 14" aria-hidden="true"><rect x="3.5" y="1" width="7" height="12" rx="1.5" fill="none" stroke="#d0202f" stroke-width="1.5"/><circle cx="7" cy="11" r="0.9" fill="#d0202f"/></svg>
        <span>+330 5187-2041</span>
      </div>
      <div class="contact__row">
        <svg viewBox="0 0 14 14" aria-hidden="true"><path d="M3 1.5 L5.2 1.5 L6 4.5 L4.6 5.6 C5.4 7.4 6.6 8.6 8.4 9.4 L9.5 8 L12.5 8.8 L12.5 11 C12.5 12 11.7 12.6 10.8 12.5 C5.8 12 2 8.2 1.5 3.2 C1.4 2.3 2 1.5 3 1.5 Z" fill="#d0202f"/></svg>
        <span>+330 5193-6672</span>
      </div>
      <div class="contact__row">
        <svg viewBox="0 0 14 14" aria-hidden="true"><rect x="1" y="3" width="12" height="8.5" rx="1" fill="none" stroke="#d0202f" stroke-width="1.4"/><path d="M1.5 3.5 L7 8 L12.5 3.5" fill="none" stroke="#d0202f" stroke-width="1.4"/></svg>
        <span>hello@meridelschool.com</span>
      </div>
      <div class="contact__row">
        <svg viewBox="0 0 14 14" aria-hidden="true"><circle cx="7" cy="7" r="5.8" fill="none" stroke="#d0202f" stroke-width="1.3"/><ellipse cx="7" cy="7" rx="2.5" ry="5.8" fill="none" stroke="#d0202f" stroke-width="1.1"/><path d="M1.2 7 H12.8" stroke="#d0202f" stroke-width="1.1"/></svg>
        <span class="contact__web">meridelschool.com</span>
      </div>
    </div>
  </section>
</main>
</body>
</html>
```